Business card for a shipping supplies business

Needing a business card design. Please see the logo. The logo with the white font should be used if there is a dark background.

We are looking for the following info on the card. Please see the sample info. We will need the info to be changed with a few different employee names and info but all will use the same template.

Business Name: The Crate Heron
Employee Name : Derek Malloy
Position: Account Manager
Address: 4827 W. Ridge 918 S.
Fort Worth, TX 72348
email: Derek@thecrateheron.com
telephone: 866-417-2902 x 217
website: www.getcartonry.com

Target Market(s)

Businesses who ship products for online sales

Industry/Entity Type

Cardboard

Contact Information for Business Card

Name, title, address, website, logo, telephone number

Font styles to use
Sans Serif

Colors
EE7325
F08F49
F5BC92
FAE3D3
FDF4ED

Requirements
Must have
• Logo on back of card. Clean look, just logo, website address

```html
<!DOCTYPE html>
<html lang="en">
<head>
<meta charset="utf-8">
<title>The Crate Heron — Business Card</title>
<link href="https://fonts.googleapis.com/css2?family=Montserrat:wght@400;500;700;800&display=swap" rel="stylesheet">
<style>
  :root {
    --backdrop: #9b9b9b;
    --paper: #f3f3f1;
    --ink: #1c1c1c;
    --card-dark: #232323;
    --orange: #ee7325;
    --orange-mid: #f08f49;
    --peach: #f5bc92;
    --edge: #c98a5e;
    --white: #ffffff;
  }
  * { box-sizing: border-box; margin: 0; padding: 0; }
  html, body { width: 1200px; height: 1050px; overflow: hidden; }
  body {
    background: var(--backdrop);
    font-family: "Montserrat", sans-serif;
    position: relative;
  }

  .card {
    position: absolute;
    border-bottom: 3px solid var(--edge);
    box-shadow: 0 10px 30px rgba(0,0,0,0.25);
  }

  /* Front — portrait */
  .card-front {
    left: 110px; top: 190px;
    width: 380px; height: 665px;
    background: var(--paper);
    padding: 56px 44px 0 48px;
  }
  .person-name {
    font-weight: 800;
    font-size: 30px;
    letter-spacing: 0.5px;
    color: var(--ink);
    line-height: 1;
  }
  .person-title {
    font-weight: 500;
    font-size: 17px;
    color: var(--orange);
    margin-top: 6px;
  }
  .divider {
    width: 22px; height: 2px;
    background: var(--peach);
    margin: 20px 0 22px;
  }
  .address {
    font-size: 15px;
    line-height: 1.45;
    color: var(--ink);
  }
  .contact-icons {
    display: flex; gap: 6px;
    margin: 18px 0 16px;
  }
  .contact-icons svg { width: 22px; height: 22px; display: block; }
  .contact-list {
    list-style: none;
    font-size: 15px;
    line-height: 1.5;
    color: var(--ink);
  }

  .front-mark {
    position: absolute;
    left: 40px; right: 40px; bottom: 44px;
    height: 250px;
    border-radius: 28px;
    background: linear-gradient(145deg, var(--peach) 0%, var(--orange-mid) 55%, var(--orange) 100%);
    display: flex; align-items: center; justify-content: center; gap: 12px;
  }
  .front-mark .mark-dot {
    width: 26px; height: 26px; border-radius: 50%;
    background: var(--ink);
  }
  .front-mark .mark-name {
    font-weight: 800;
    font-size: 26px;
    color: var(--ink);
    letter-spacing: 0.5px;
  }

  /* Back — landscape */
  .card-back {
    left: 560px; top: 360px;
    width: 580px; height: 332px;
    background: var(--card-dark);
    display: flex; flex-direction: column; align-items: center; justify-content: center;
  }
  .back-mark {
    display: flex; align-items: center; gap: 14px;
  }
  .back-mark .mark-dot {
    width: 40px; height: 40px; border-radius: 50%;
    background: var(--orange);
  }
  .back-mark .mark-name {
    font-weight: 800;
    font-size: 38px;
    letter-spacing: 1px;
    color: var(--white);
  }
  .website {
    margin-top: 34px;
    display: flex; align-items: center; gap: 8px;
    font-weight: 500;
    font-size: 17px;
    color: var(--white);
  }
  .website svg { width: 20px; height: 20px; display: block; }
</style>
</head>
<body>

  <section class="card card-front" aria-label="Card front">
    <h1 class="person-name">DEREK MALLOY</h1>
    <p class="person-title">Account Manager</p>
    <div class="divider"></div>
    <p class="address">4827 W. Ridge 918 S.<br>Fort Worth, TX 72348</p>

    <div class="contact-icons" aria-hidden="true">
      <svg viewBox="0 0 22 22"><circle cx="11" cy="11" r="11" fill="var(--orange)"/><path d="M7.5 6.5c.6-.6 1.4-.5 1.8.1l.8 1.3c.3.5.2 1.1-.2 1.4l-.6.5c.5 1.2 1.6 2.3 2.8 2.8l.5-.6c.4-.4 1-.5 1.4-.2l1.3.8c.6.4.7 1.2.1 1.8l-.6.6c-.9.9-3.3.1-5.2-1.8S6 8 6.9 7.1z" fill="#fff"/></svg>
      <svg viewBox="0 0 22 22"><circle cx="11" cy="11" r="11" fill="var(--orange)"/><rect x="6" y="7.5" width="10" height="7" rx="1" fill="#fff"/><path d="M6.3 8l4.7 3.6L15.7 8" stroke="var(--orange)" stroke-width="1" fill="none"/></svg>
      <svg viewBox="0 0 22 22"><circle cx="11" cy="11" r="11" fill="var(--orange)"/><circle cx="11" cy="11" r="5" fill="none" stroke="#fff" stroke-width="1.4"/><path d="M6 11h10M11 6c-2 3-2 7 0 10M11 6c2 3 2 7 0 10" stroke="#fff" stroke-width="1" fill="none"/></svg>
    </div>

    <ul class="contact-list">
      <li>866-417-2902 x 217</li>
      <li>Derek@thecrateheron.com</li>
      <li>getcartonry.com</li>
    </ul>

    <div class="front-mark" role="img" aria-label="Company mascot emblem area: The Crate Heron">
      <span class="mark-dot"></span>
      <span class="mark-name">THE CRATE HERON</span>
    </div>
  </section>

  <section class="card card-back" aria-label="Card back">
    <div class="back-mark">
      <span class="mark-dot"></span>
      <span class="mark-name">THE CRATE HERON</span>
    </div>
    <p class="website">
      <svg viewBox="0 0 20 20" aria-hidden="true"><circle cx="10" cy="10" r="10" fill="var(--orange)"/><circle cx="10" cy="10" r="4.5" fill="none" stroke="var(--card-dark)" stroke-width="1.4"/><path d="M5.5 10h9M10 5.5c-1.8 2.7-1.8 6.3 0 9M10 5.5c1.8 2.7 1.8 6.3 0 9" stroke="var(--card-dark)" stroke-width="1" fill="none"/></svg>
      getcartonry.com
    </p>
  </section>

</body>
</html>
```